BrightKeel Business Card Contest

We are looking for a modern business card that catches attention and is unique. Attached is the brand guide and logo files. Please note that the back side (not the side with our name and info) with be UV raise printed, so have fun with the design there. We want to include Name, Title, Phone number, email, website.

Contact Information for Business Card

Please see project description

```html
<!DOCTYPE html>
<html lang="en">
<head>
<meta charset="utf-8">
<title>BrightKeel Business Card</title>
<link rel="stylesheet" href="https://fonts.googleapis.com/css2?family=Montserrat:wght@500;800&family=Poppins:wght@500&display=swap">
<style>
  :root {
    --page: #3a3a3c;
    --card: #161617;
    --card-edge: #e0302a;
    --accent: #e4312b;
    --ink: #ffffff;
    --uv-ink: #2a2a2c;
    --uv-shine: #1d1d1f;
  }
  * { box-sizing: border-box; margin: 0; padding: 0; }
  html, body { width: 1200px; height: 875px; overflow: hidden; }
  body {
    background: var(--page);
    font-family: "Poppins", sans-serif;
    display: flex;
    align-items: center;
    justify-content: center;
    gap: 40px;
  }
  .card {
    position: relative;
    width: 540px;
    height: 310px;
    border-radius: 22px;
    background: var(--card);
    border-bottom: 4px solid var(--card-edge);
    border-left: 2px solid var(--card-edge);
    overflow: hidden;
  }

  /* UV raised back side */
  .card--back {
    background: linear-gradient(135deg, #2a2a2c 0%, var(--card) 45%, var(--uv-shine) 100%);
  }
  .back-brand {
    position: absolute;
    left: 50%;
    top: 50%;
    transform: translate(-50%, -50%);
    display: flex;
    align-items: center;
    gap: 18px;
  }
  .back-brand__square {
    width: 46px;
    height: 46px;
    background: var(--uv-ink);
  }
  .back-brand__name {
    font-family: "Poppins", sans-serif;
    font-weight: 500;
    font-size: 64px;
    letter-spacing: -1px;
    color: var(--uv-ink);
  }

  /* Info front side */
  .brand {
    position: absolute;
    left: 44px;
    top: 62px;
    display: flex;
    align-items: center;
    gap: 12px;
  }
  .brand__square {
    width: 26px;
    height: 26px;
    background: var(--ink);
  }
  .brand__name {
    font-weight: 500;
    font-size: 38px;
    color: var(--ink);
    letter-spacing: -0.5px;
  }
  .person {
    position: absolute;
    right: 40px;
    top: 46px;
    text-align: right;
  }
  .person__name {
    font-family: "Montserrat", sans-serif;
    font-weight: 800;
    font-size: 25px;
    color: var(--accent);
  }
  .person__title {
    font-family: "Montserrat", sans-serif;
    font-weight: 500;
    font-size: 14px;
    color: var(--ink);
    margin-top: 2px;
  }
  .address {
    position: absolute;
    left: 48px;
    top: 150px;
    font-size: 14px;
    line-height: 1.45;
    color: var(--ink);
  }
  .contacts {
    position: absolute;
    left: 48px;
    top: 208px;
    list-style: none;
    font-size: 14px;
    color: var(--ink);
  }
  .contacts li {
    display: flex;
    align-items: center;
    gap: 10px;
    line-height: 1.55;
  }
  .contacts svg { width: 13px; height: 13px; fill: var(--accent); flex: none; }
</style>
</head>
<body>
  <section class="card card--back" aria-label="Card back, UV raised print">
    <div class="back-brand">
      <span class="back-brand__square"></span>
      <span class="back-brand__name">BrightKeel</span>
    </div>
  </section>

  <section class="card card--front" aria-label="Card front with contact details">
    <div class="brand">
      <span class="brand__square"></span>
      <span class="brand__name">BrightKeel</span>
    </div>
    <div class="person">
      <p class="person__name">Mark Halvorsen</p>
      <p class="person__title">Managing Director</p>
    </div>
    <p class="address">P.O. Box 2740<br>Lake Harlow, WA 98120</p>
    <ul class="contacts">
      <li>
        <svg viewBox="0 0 24 24" aria-hidden="true"><path d="M6.6 10.8a15.1 15.1 0 0 0 6.6 6.6l2.2-2.2a1 1 0 0 1 1-.25 11.4 11.4 0 0 0 3.6.57 1 1 0 0 1 1 1V20a1 1 0 0 1-1 1A17 17 0 0 1 3 4a1 1 0 0 1 1-1h3.5a1 1 0 0 1 1 1c0 1.25.2 2.45.57 3.57a1 1 0 0 1-.25 1z"/></svg>
        555 210 480
      </li>
      <li>
        <svg viewBox="0 0 24 24" aria-hidden="true"><path d="M2 5h20v14H2z M4 7v.4l8 5.2 8-5.2V7z" fill-rule="evenodd"/></svg>
        info@brightkeel.com
      </li>
      <li>
        <svg viewBox="0 0 24 24" aria-hidden="true"><path d="M12 2a10 10 0 1 0 0 20 10 10 0 0 0 0-20zm6.9 6h-3a15 15 0 0 0-1.4-3.9A8 8 0 0 1 18.9 8zM12 4a13 13 0 0 1 1.9 4h-3.8A13 13 0 0 1 12 4zM4.3 14a8 8 0 0 1 0-4h3.4a16 16 0 0 0 0 4zm.8 2h3a15 15 0 0 0 1.4 3.9A8 8 0 0 1 5.1 16zm3-8h-3a8 8 0 0 1 4.4-3.9A15 15 0 0 0 8.1 8zM12 20a13 13 0 0 1-1.9-4h3.8A13 13 0 0 1 12 20zm2.3-6H9.7a14 14 0 0 1 0-4h4.6a14 14 0 0 1 0 4zm.2 5.9a15 15 0 0 0 1.4-3.9h3a8 8 0 0 1-4.4 3.9zM16.3 14a16 16 0 0 0 0-4h3.4a8 8 0 0 1 0 4z"/></svg>
        www.brightkeel.com
      </li>
    </ul>
  </section>
</body>
</html>
```